Grain Clear Kitchen Web Design

We are looking for designs for a homepage for a gluten free, health food website.

We are looking for the site to be a shop, as well as a resource/information source for users. We will also look to incorporate recipes, blogs, forums and potentially some other useful information.

We want to ensure that the website is user-friendly, does not have a corporate feel, but is still classy.

We want to have high quality photographic images in the background, with text in the foreground - but these things will need to compliment each other well. e.g recipe of the week integrated onto the background photo and the 'shop' in the foreground.

We have seen a site that we quite like and although we like the design, we do not want to completely emulate this. However, it is a useful starting point for designers and perhaps some inspiration www.brightpantryhall.example

We already have a logo - see attached - which will need to be fully integrated into the design.

We do want a colourful design, but mainly in terms of the images rather than the graphics.
Updates

Please note:

We are pleased with the designs to date, for the most part. We would like you all to note, however, that we are much preferring the lighter designs - ones that make the sites feel brighter - rather than those which are darker in appearance.

We would also like to see less space allocated to the main image, within the context of the site as a whole.

Thanks.

We have eliminated those which we feel are not what we are looking for. We are still keen to see some more designs and are still looking for something unique. There are some good things in all of the designs that we have not eliminated, however we still feel there is room for more inspiration.

Thanks.

Target Market(s)

Our audience are body conscience people looking for health food products. They are also those who are potentially looking for a new lifestyle/life cha

Industry/Entity Type

Health

Requirements
Must have
• Our logo - attached, can provide variations in due course.

Navigational features as per mock up attached.

Social network integration.

NB: we only need one (home) page for this.

```html
<!DOCTYPE html>
<html lang="en">
<head>
<meta charset="utf-8">
<title>Grain Clear Kitchen</title>
<link href="https://fonts.googleapis.com/css2?family=Ropa+Sans&family=Source+Sans+3:wght@300;400&display=swap" rel="stylesheet">
<style>
:root{
  --ink:#2b2b2b;
  --nav-ink:#2f3033;
  --menu-bg:#3a3a3c;
  --menu-dark:#232325;
  --menu-line:#4a4a4c;
  --accent:#f07a28;
  --body-text:#5a5a5a;
  --card-border:#e4e4e4;
  --button-bg:#ececec;
  --footer-bg:#efefef;
  --white:#ffffff;
}
*{margin:0;padding:0;box-sizing:border-box}
html,body{width:1031px;height:1200px;overflow:hidden;background:var(--white)}
body{position:relative;font-family:"Source Sans 3",sans-serif;color:var(--body-text)}
.hero{position:absolute;left:0;top:0;width:1031px;height:574px;
  background:radial-gradient(ellipse at 30% 60%,#e9c9a3 0%,transparent 45%),
  radial-gradient(ellipse at 75% 35%,#d9524a 0%,transparent 35%),
  radial-gradient(ellipse at 55% 70%,#7aa84a 0%,transparent 30%),
  linear-gradient(135deg,#cfd3cf 0%,#e4b996 40%,#c98a64 70%,#b7c1b0 100%)}
.header{position:absolute;left:0;top:0;width:1031px;height:116px;background:rgba(255,255,255,.82)}
.brand{position:absolute;left:51px;top:38px;font-family:"Ropa Sans",sans-serif;font-size:30px;color:var(--ink);display:flex;align-items:center;gap:10px}
.brand-mark{width:22px;height:22px;background:var(--ink)}
.top-nav{position:absolute;top:56px;left:518px;display:flex;font-family:"Ropa Sans",sans-serif;font-size:20px;color:var(--nav-ink)}
.top-nav span{margin-right:14px}
.top-nav .sep{color:#999;font-size:14px;margin-top:4px}
.search{position:absolute;left:789px;top:55px;width:201px;height:27px;border:1px solid #d4d4d4;border-radius:14px;background:var(--white);font-size:12px;color:#888;padding:6px 14px}
.search svg{position:absolute;right:9px;top:6px}
.side-menu{position:absolute;left:37px;top:169px;width:194px;border-top:7px solid var(--accent);font-family:"Ropa Sans",sans-serif}
.side-menu div{height:36px;line-height:36px;padding-left:34px;background:var(--menu-bg);color:var(--white);font-size:17px;border-bottom:1px solid var(--menu-line)}
.side-menu .active{background:var(--menu-dark)}
.sub-menu{position:absolute;left:231px;top:323px;width:169px}
.sub-menu div{height:36px;line-height:36px;padding-left:17px;background:var(--menu-dark);color:var(--white);font-size:14px;margin-bottom:1px}
.dots{position:absolute;left:481px;top:519px;display:flex;gap:3px}
.dots i{width:14px;height:14px;border-radius:50%;background:var(--white)}
.dots i:first-child{border:2px solid var(--ink)}
.card{position:absolute;top:546px;width:297px;height:329px;background:var(--white);border:1px solid var(--card-border);box-shadow:0 1px 3px rgba(0,0,0,.08)}
.card-image{position:absolute;left:13px;top:13px;width:271px;height:142px}
.card h2{position:absolute;left:20px;top:172px;font-family:"Ropa Sans",sans-serif;font-weight:400;font-size:23px;color:var(--ink)}
.card p{position:absolute;left:20px;top:204px;width:262px;font-weight:300;font-size:12.5px;line-height:19px}
.card .more{position:absolute;left:18px;top:271px;height:28px;line-height:28px;padding:0 11px 0 13px;background:var(--button-bg);border-radius:2px;font-family:"Ropa Sans",sans-serif;font-size:11.5px;color:#555;text-transform:uppercase}
.footer{position:absolute;left:0;top:938px;width:1031px;height:262px;background:var(--footer-bg);border-top:1px dashed #c8c8c8}
.footer h3{position:absolute;font-family:"Ropa Sans",sans-serif;font-weight:400;font-size:17px;color:var(--ink);top:48px}
.links{position:absolute;top:79px;list-style:none;font-size:12.5px;color:#555}
.links li{height:25.5px}
.links li::before{content:"\25B8";font-size:8px;color:#777;margin-right:7px;vertical-align:2px}
.social{position:absolute;left:583px;top:71px;display:flex;gap:5px}
.social i{width:28px;height:28px;border-radius:50%;background:#111}
.copyright{position:absolute;left:74px;top:220px;font-size:11px;color:#555}
</style>
</head>
<body>
<div class="hero" role="img" aria-label="Close-up photo of open sandwiches with ham, cheese, tomato and basil"></div>
<header class="header">
  <div class="brand"><span class="brand-mark"></span>Grain Clear Kitchen</div>
  <nav class="top-nav"><span>Home</span><span class="sep">|</span><span>Log In</span><span class="sep">|</span><span>Contact Us</span></nav>
  <div class="search">Search here
    <svg width="15" height="15" viewBox="0 0 15 15"><circle cx="6" cy="6" r="4.5" fill="none" stroke="#999" stroke-width="2"/><line x1="9.5" y1="9.5" x2="13.5" y2="13.5" stroke="#999" stroke-width="2"/></svg>
  </div>
</header>
<nav class="side-menu">
  <div>SHOP</div><div>OUR STORY</div><div>BLOG</div><div>HINTS &amp; TIPS</div><div class="active">RECIPES</div><div>FORUMS</div>
</nav>
<nav class="sub-menu"><div>Kids Pizza</div><div>Gluten Free Scones</div><div>More Recepies</div></nav>
<div class="dots"><i></i><i></i><i></i><i></i></div>

<section class="card" style="left:44px">
  <div class="card-image" role="img" aria-label="Photo of a woman eating a fresh salad" style="background:linear-gradient(120deg,#8a5a3e,#d8b49a 50%,#e8e4de)"></div>
  <h2>Featured Recipes</h2>
  <p>Duis tincidunt lectus quis dui viverra vestibulum. Suspendisse vulputate aliquam dui. Nulla elementum dui ut augue.</p>
  <div class="more">More Recipes ▸</div>
</section>
<section class="card" style="left:368px">
  <div class="card-image" role="img" aria-label="Photo of a fork holding a bite of salad" style="background:linear-gradient(120deg,#e6e8e8,#f2ece6 50%,#d8c2b4)"></div>
  <h2>Recent Blog Post</h2>
  <p>Duis tincidunt lectus quis dui viverra vestibulum. Suspendisse vulputate aliquam dui. Nulla elementum dui ut augue.</p>
  <div class="more">More Blog ▸</div>
</section>
<section class="card" style="left:691px">
  <div class="card-image" role="img" aria-label="Photo of hands chopping mushrooms and vegetables" style="background:linear-gradient(120deg,#c9c2b6,#e9dccb 45%,#d6a34a 75%,#c4442e)"></div>
  <h2>Hints &amp; Tips</h2>
  <p>Duis tincidunt lectus quis dui viverra vestibulum. Suspendisse vulputate aliquam dui. Nulla elementum dui ut augue.</p>
  <div class="more">More Hits &amp; Tips ▸</div>
</section>

<footer class="footer">
  <h3 style="left:74px">QUICK LINKS</h3>
  <ul class="links" style="left:74px"><li>Home</li><li>Shop Now</li><li>Our Story</li><li>Hints &amp; Tips</li></ul>
  <ul class="links" style="left:243px"><li>Our Recipes</li><li>Forums</li><li>Contact Us</li><li>FAQ's</li></ul>
  <ul class="links" style="left:411px"><li>Sitemap</li><li>Privacy Policy</li><li>Term &amp; Use</li></ul>
  <h3 style="left:583px">GET CONNECTED</h3>
  <div class="social"><i></i><i></i><i></i><i></i></div>
  <div class="copyright">© 2012 Company Name.&nbsp; All right reserved.&nbsp; Term of Use</div>
</footer>
</body>
</html>
```